Brook Forge - Crypto Currency Miner Powered by Renewable Energy Website

We Need Web Pages Design for Website for Crypto Currency Miner

Serivices include:
Mining Rig Sales
Housing for Rigs turnkey on renewable energy grid
Cloud Mining term packages
Updates

http://www.vaultrigdigest.example (Competitors sites)

Target Market(s)

Investers for Mining Rigs and terms for 1,2 or 3 years of Hash rate

Industry/Entity Type

Mining

Number of Pages Required

5+ page

Font styles to use
Sans Serif

Colors
add136
9bcb3c
606060
474747
ffc214
cadf82
fbee3e
876aae
6b449b

Requirements
Must have
• Pictures of Solar, Wind and power Factor Correction units
Nice to have
• e-commerce platform so contract terms can be purchased through website
Should not have
• Heavy construction equipment

```html
<!DOCTYPE html>
<html lang="en">
<head>
<meta charset="utf-8">
<title>Brook Forge — Renewable Crypto Mining</title>
<link href="https://fonts.googleapis.com/css2?family=Open+Sans:wght@400;600;700;800&display=swap" rel="stylesheet">
<style>
:root{
  --green:#2e9e3f;
  --green-mid:#4fae3a;
  --lime:#9bcb3c;
  --grey:#606060;
  --dark:#474747;
  --ink:#262626;
  --yellow:#ffc214;
  --pale:#cadf82;
  --white:#ffffff;
}
*{margin:0;padding:0;box-sizing:border-box}
html,body{width:1200px;height:1192px;overflow:hidden;background:var(--white);font-family:"Open Sans",sans-serif;color:var(--ink)}
.page{position:relative;width:1200px;height:1192px;overflow:hidden}

.site-header{position:absolute;left:0;top:0;width:1200px;height:82px;background:var(--white);z-index:3}
.contact-bar{position:absolute;left:116px;top:0;width:368px;height:44px;border-bottom:1px solid #e4e4e4;display:flex;align-items:center;font-size:10px;color:var(--ink)}
.contact-bar .item{display:flex;align-items:center;gap:5px;padding:0 10px 0 25px;height:100%}
.contact-bar .item+.item{border-left:1px solid #e4e4e4;padding-left:10px}
.right-rule{position:absolute;left:716px;top:43px;width:368px;border-top:1px solid #e4e4e4}
.nav{position:absolute;top:53px;display:flex;align-items:center;font-size:11px;font-weight:600;text-transform:uppercase;letter-spacing:.2px}
.nav a{color:var(--ink);text-decoration:none}
.nav a.active{color:var(--green)}
.nav .dot{width:5px;height:5px;border-radius:50%;background:var(--green);margin:0 34px}
.nav-left{left:143px}
.nav-right{left:775px}
.nav-right .dot{margin:0 33px}

.brand{position:absolute;left:484px;top:0;width:230px;height:136px;background:var(--white);border-radius:0 0 30px 30px;z-index:4;display:flex;flex-direction:column;align-items:center;justify-content:flex-end;padding-bottom:16px}
.brand .mark{width:70px;height:70px;border-radius:50%;background:var(--green-mid);margin-bottom:10px}
.brand .name{font-size:30px;font-weight:700;color:var(--grey);line-height:1}

.auth{position:absolute;top:9px;display:flex;align-items:center;justify-content:center;gap:6px;height:25px;width:109px;color:var(--white);font-size:10px;font-weight:600}
.auth.login{left:812px;background:linear-gradient(90deg,var(--green),#49b43a)}
.auth.signup{left:926px;background:var(--grey)}
.cart{position:absolute;left:1054px;top:12px}
.cart .badge{position:absolute;right:-3px;top:-3px;width:6px;height:6px;border-radius:50%;background:var(--yellow)}

.hero{position:absolute;left:0;top:82px;width:1200px;height:478px;background:linear-gradient(180deg,#cfe2c7 0%,#e6efdc 45%,#b9c878 62%,#7f9b2e 80%,#5e7a1e 100%)}
.hero-title{position:absolute;left:408px;top:110px;font-size:78px;font-weight:800;line-height:60px;color:var(--white);letter-spacing:-1px;text-shadow:0 6px 10px rgba(0,0,0,.18)}
.hero-band{position:absolute;left:0;top:560px;width:1200px;height:40px;background:#dbe8d4}
.slider-dots{position:absolute;left:1075px;top:238px;display:flex;flex-direction:column;gap:15px;z-index:2}
.slider-dots span{width:9px;height:9px;border-radius:50%;background:var(--white)}
.slider-dots span.on{background:var(--green-mid)}

.sketch{position:absolute;left:1084px;top:690px;width:116px;height:282px;background:linear-gradient(160deg,#ffffff 0%,#f2f2f2 55%,#d9d9d9 100%)}

.services{position:absolute;left:116px;top:547px;width:968px;height:375px;background:var(--white);box-shadow:0 4px 22px rgba(0,0,0,.12);z-index:2}
.services h2{position:absolute;left:0;width:100%;top:34px;text-align:center;font-size:33px;font-weight:800;color:var(--ink)}
.service{position:absolute;width:220px;text-align:center;font-size:14px;line-height:17px;color:var(--ink)}
.service .ring{width:96px;height:96px;border-radius:50%;border:1px solid var(--ink);margin:0 auto 17px;display:flex;align-items:center;justify-content:center;background:var(--white)}
.service.featured{color:var(--green)}
.service.featured .ring{border-color:var(--green);box-shadow:0 4px 14px rgba(0,0,0,.12)}
.service.s1{left:109px;top:87px}
.service.s2{left:372px;top:99px}
.service.s3{left:639px;top:99px}
.btn-more{position:absolute;left:438px;top:297px;width:92px;height:29px;border-radius:15px;background:var(--yellow);color:var(--white);font-size:10px;font-weight:700;display:flex;align-items:center;justify-content:center}

.about-visual{position:absolute;left:0;top:972px;width:426px;height:220px;background:linear-gradient(180deg,#3c9be0 0%,#7cc0ee 55%,#6aa83a 80%,#4a8a2a 100%)}
.about{position:absolute;left:426px;top:972px;width:774px;height:220px;background:linear-gradient(110deg,#3ea83a 0%,#56b23c 50%,#86c23e 100%);color:var(--white);padding:62px 0 0 38px}
.about .eyebrow{display:flex;align-items:center;gap:12px;font-size:16px;letter-spacing:5px;font-weight:400}
.about h3{font-size:32px;font-weight:800;margin-top:4px;line-height:40px}
.about p{margin-top:12px;width:570px;font-size:11.6px;line-height:17.6px}
</style>
</head>
<body>
<div class="page">

  <header class="site-header">
    <div class="contact-bar">
      <span class="item">
        <svg width="10" height="10" viewBox="0 0 24 24"><path fill="#2e9e3f" d="M6.6 10.8a15 15 0 0 0 6.6 6.6l2.2-2.2c.3-.3.7-.4 1-.2 1.1.4 2.3.6 3.6.6.6 0 1 .4 1 1V20c0 .6-.4 1-1 1A17 17 0 0 1 3 4c0-.6.4-1 1-1h3.5c.6 0 1 .4 1 1 0 1.3.2 2.5.6 3.6.1.3 0 .7-.2 1z"/></svg>
        012 - 555 - 0148
      </span>
      <span class="item">
        <svg width="12" height="9" viewBox="0 0 24 18"><rect x="1" y="1" width="22" height="16" fill="none" stroke="#2e9e3f" stroke-width="2"/><path d="M1 1l11 9 11-9" fill="none" stroke="#2e9e3f" stroke-width="2"/></svg>
        info@brookforge.example
      </span>
    </div>
    <div class="right-rule"></div>

    <nav class="nav nav-left">
      <a class="active" href="#">Home</a><span class="dot"></span>
      <a href="#">About Us</a><span class="dot"></span>
      <a href="#">Services</a>
    </nav>
    <nav class="nav nav-right">
      <a href="#">Package</a><span class="dot"></span>
      <a href="#">Blog</a><span class="dot"></span>
      <a href="#">Contact Us</a>
    </nav>

    <a class="auth login" href="#">
      <svg width="9" height="10" viewBox="0 0 20 22"><circle cx="10" cy="6" r="5" fill="#fff"/><path d="M0 22c0-6 4-9 10-9s10 3 10 9z" fill="#fff"/></svg>
      Login
    </a>
    <a class="auth signup" href="#">
      <svg width="10" height="10" viewBox="0 0 20 20"><rect x="2" y="3" width="12" height="15" fill="none" stroke="#fff" stroke-width="2"/><path d="M16 1l3 3-9 9H7v-3z" fill="#fff"/></svg>
      Sign Up
    </a>
    <div class="cart">
      <svg width="20" height="18" viewBox="0 0 24 22"><path d="M1 2h4l3 12h12l3-9H7" fill="none" stroke="#474747" stroke-width="2.4"/><circle cx="9" cy="19" r="2" fill="#474747"/><circle cx="19" cy="19" r="2" fill="#474747"/></svg>
      <span class="badge"></span>
    </div>
  </header>

  <div class="brand">
    <span class="mark"></span>
    <span class="name">Brook Forge</span>
  </div>

  <section class="hero" role="img" aria-label="Illustrated countryside with wind turbines, a power pylon, solar panels and a house with rooftop solar under a pale green sky">
    <h1 class="hero-title">THE<br>BROOK<br>FORGE</h1>
    <div class="slider-dots"><span class="on"></span><span></span><span></span><span></span></div>
  </section>
  <div class="hero-band"></div>

  <div class="sketch" role="img" aria-label="Faint pencil sketch of wind turbines and solar arrays"></div>

  <section class="services">
    <h2>SERVICES</h2>

    <div class="service featured s1">
      <div class="ring">
        <svg width="36" height="48" viewBox="0 0 36 48">
          <circle cx="18" cy="4" r="3" fill="#2e9e3f"/>
          <path d="M18 7v5M8 12h20M8 12v8M28 12v8M13 16h10M13 16v4M23 16v4" fill="none" stroke="#2e9e3f" stroke-width="1.5"/>
          <rect x="2" y="20" width="14" height="26" fill="none" stroke="#2e9e3f" stroke-width="2"/>
          <rect x="20" y="20" width="14" height="26" fill="none" stroke="#2e9e3f" stroke-width="2"/>
          <path d="M4 34h10l-5 10zM22 34h10l-5 10z" fill="#2e9e3f"/>
        </svg>
      </div>
      Mining Rig Sales
    </div>

    <div class="service s2">
      <div class="ring">
        <svg width="54" height="42" viewBox="0 0 54 42">
          <path d="M6 2v38M3 6h6M3 11h6M9 8l4 4M13 4v36" fill="none" stroke="#262626" stroke-width="2"/>
          <path d="M14 40V22L32 10l18 12v18z" fill="none" stroke="#262626" stroke-width="2"/>
          <rect x="22" y="24" width="20" height="12" fill="none" stroke="#262626" stroke-width="2"/>
          <path d="M22 30h20M32 24v12" stroke="#262626" stroke-width="1.5"/>
          <path d="M2 40h52" stroke="#262626" stroke-width="2"/>
        </svg>
      </div>
      Housing for Rigs<br>Turnkey on Renewable<br>Energy Grid
    </div>

    <div class="service s3">
      <div class="ring">
        <svg width="46" height="42" viewBox="0 0 46 42">
          <path d="M10 26a8 8 0 0 1 0-16 11 11 0 0 1 21-3 9 9 0 0 1 6 19z" fill="none" stroke="#262626" stroke-width="2"/>
          <path d="M14 26v6M20 26v10M26 26v10M32 26v6" stroke="#262626" stroke-width="2"/>
          <circle cx="14" cy="34" r="2" fill="none" stroke="#262626" stroke-width="1.6"/>
          <circle cx="20" cy="38" r="2" fill="none" stroke="#262626" stroke-width="1.6"/>
          <circle cx="26" cy="38" r="2" fill="none" stroke="#262626" stroke-width="1.6"/>
          <circle cx="32" cy="34" r="2" fill="none" stroke="#262626" stroke-width="1.6"/>
        </svg>
      </div>
      Cloud Mining<br>Term Packages
    </div>

    <a class="btn-more" href="#">VIEW MORE</a>
  </section>

  <div class="about-visual" role="img" aria-label="Illustration of a house with rooftop solar panels and wind turbines on green hills under a blue sky"></div>

  <section class="about">
    <div class="eyebrow">ABOUT
      <svg width="26" height="32" viewBox="0 0 26 32"><path d="M24 1C10 3 2 10 4 24l-3 7 2 1 3-7C20 26 26 14 24 1z" fill="#fff"/></svg>
    </div>
    <h3>THE BROOK FORGE</h3>
    <p>Lorem ipsum dolor sit amet, consectetur adipiscing elit. Pellentesque eget feugiat nibh. Sed venenatis mi non egestas euismod. Etiam cursus risus non ante pretium ultricies. Nam et condimentum ex. Phasellus varius lectus nec porta vehicula. Etiam mollis nisi vel lectus dignissim consequat. Donec vel tellus orci. Donec mollis nunc est,</p>
  </section>

</div>
</body>
</html>
```